Photojournalism/photography business needs a simple, timeless & professional letterhead design

We need a letterhead design for photography/photojournalism business called 'plomk', no capitals.

The letterhead needs to be:
- simple
- professional
- timeless
- easy to read
- consists of at least 2 colors to make it stands out.

We do mainly editorial photography, photo articles for various publications, travel, businesses, as well as people such as family and kids.

The final design should communicate professionalism, easy identification, attention grabbing, even if it has to be found among a stack of various papers on the clients' desks.

Target Market(s)

Various publications.

Industry/Entity Type

Business

Requirements
Must have
• Please use the logo attached.

```html
<!DOCTYPE html>
<html lang="en">
<head>
<meta charset="utf-8">
<title>plomk – Letterhead Concept</title>
<link href="https://fonts.googleapis.com/css2?family=Nunito+Sans:wght@400;800&display=swap" rel="stylesheet">
<style>
  :root {
    --brand-blue: #1ab0ea;
    --slate: #6d6e71;
    --ink: #58595b;
    --rule: #7a7b7e;
    --paper: #ffffff;
  }
  * { margin: 0; padding: 0; box-sizing: border-box; }
  html, body { width: 1200px; height: 927px; overflow: hidden; background: var(--paper); }
  body { position: relative; font-family: "Nunito Sans", Arial, sans-serif; color: var(--ink); }

  .sheet { position: absolute; top: 120px; width: 465px; height: 601px; border: 1px solid #555; background: var(--paper); }
  .sheet--first { left: 137px; }
  .sheet--second { left: 613px; }

  .wordmark { position: absolute; font-weight: 800; color: var(--brand-blue); letter-spacing: -0.5px; line-height: 1; white-space: nowrap; }
  .wordmark--sheet { font-size: 27px; }
  .wordmark--card { font-size: 24px; }
  .wordmark--card-back { font-size: 28px; }

  .divider { position: absolute; width: 1px; background: var(--ink); }
  .contact { position: absolute; font-size: 5.2px; line-height: 7px; color: var(--ink); white-space: nowrap; }
  .contact--card { font-size: 4.6px; line-height: 6px; }
  .band { position: absolute; background: var(--slate); }
  .tab-blue { position: absolute; background: var(--brand-blue); }

  .card { position: absolute; top: 478px; width: 192px; height: 110px; }
  .card--front { left: 81px; background: var(--paper); border: 1px solid #555; }
  .card--back { left: 283px; background: var(--slate); }
  .card__person { position: absolute; left: 105px; top: 12px; font-size: 5px; line-height: 7px; color: var(--brand-blue); white-space: nowrap; }
  .card__rule { position: absolute; width: 1px; background: #fff; }

  .footer-rule { position: absolute; left: 27px; top: 823px; width: 1146px; height: 2px; background: var(--rule); }
  .caption-rule { position: absolute; left: 886px; top: 836px; width: 2px; height: 65px; background: var(--rule); }
  .caption { position: absolute; left: 904px; top: 848px; font-size: 15px; line-height: 19px; color: var(--ink); }
</style>
</head>
<body>

  <section class="sheet sheet--first" aria-label="Letterhead, first page">
    <div class="tab-blue" style="left:0;top:46px;width:14px;height:32px;"></div>
    <div class="wordmark wordmark--sheet" style="left:23px;top:47px;">plomk</div>
    <div class="divider" style="left:111px;top:47px;height:31px;"></div>
    <div class="contact" style="left:123px;top:48px;">
      000 Company Address<br>City, State, Country, Zip Code<br>T: 000.000.0000 F: 000.000.0000<br>www.plomk.com
    </div>
    <div class="band" style="left:211px;top:46px;width:253px;height:32px;"></div>
  </section>

  <section class="sheet sheet--second" aria-label="Letterhead, continuation page">
    <div class="band" style="left:0;top:42px;width:264px;height:32px;"></div>
    <div class="wordmark wordmark--sheet" style="left:271px;top:43px;">plomk</div>
    <div class="divider" style="left:359px;top:42px;height:32px;"></div>
    <div class="contact" style="right:18px;top:44px;text-align:right;">
      000 Company Address<br>City, State, Country, Zip Code<br>T: 000.000.0000 F: 000.000.0000<br>www.plomk.com
    </div>
    <div class="band" style="left:450px;top:42px;width:14px;height:32px;"></div>
  </section>

  <section class="card card--front" aria-label="Business card, front">
    <div class="card__person">Person's Name<br>Job Title</div>
    <div class="tab-blue" style="left:0;top:38px;width:13px;height:32px;"></div>
    <div class="wordmark wordmark--card" style="left:21px;top:41px;">plomk</div>
    <div class="divider" style="left:97px;top:40px;height:30px;"></div>
    <div class="contact contact--card" style="left:104px;top:41px;">
      000 Company Address<br>City, State, Country, Zip Code<br>T: 000.000.0000 F: 000.000.0000<br>www.plomk.com
    </div>
    <div class="band" style="left:177px;top:38px;width:14px;height:32px;"></div>
  </section>

  <section class="card card--back" aria-label="Business card, back">
    <div class="card__rule" style="left:69px;top:33px;height:40px;"></div>
    <div class="wordmark wordmark--card-back" style="left:84px;top:38px;">plomk</div>
    <div class="card__rule" style="left:178px;top:33px;height:40px;"></div>
  </section>

  <div class="footer-rule"></div>
  <div class="caption-rule"></div>
  <div class="caption">plomk<br>Letterhead Concept - Version 2</div>

</body>
</html>
```